Property investment company needs a letterhead design!

We are a new residential and commercial property investment company. Name of the company is Morvesta Group, LLC. We have a new logo and now we need letterhead! We prefer to have a professional and upscale appearance. We don't have any fixed requirements, so be creative! Thank you for considering this project. We are so excited to see what happens!

Target Market(s)

Professional

Industry/Entity Type

Real Estate Development

```html
<!DOCTYPE html>
<html lang="en">
<head>
<meta charset="utf-8">
<title>Morvesta Group, LLC – Letterhead</title>
<link rel="stylesheet" href="https://fonts.googleapis.com/css2?family=Roboto:wght@400;500;700&family=Open+Sans:wght@400&display=swap">
<style>
  :root{
    --backdrop:#e4e4e4;
    --paper:#f1f2f2;
    --navy:#060c24;
    --cyan:#01a2c9;
    --ink:#2f3640;
    --map:#e3e5e8;
  }
  *{box-sizing:border-box;margin:0;padding:0}
  html,body{width:1200px;height:1200px;overflow:hidden}
  body{background:var(--backdrop);font-family:"Roboto",sans-serif;color:var(--ink)}
  .letterhead{position:absolute;left:252px;top:108px;width:696px;height:984px;background:var(--paper);overflow:hidden}
  .world-map{position:absolute;left:102px;top:16px;width:460px;height:286px;border-radius:45% 45% 40% 40%;background:radial-gradient(ellipse at center,var(--map) 0%,rgba(227,229,232,.6) 55%,rgba(241,242,242,0) 75%)}
  .brand{position:absolute;left:0;width:696px;top:100px;display:flex;justify-content:center;align-items:center;gap:10px}
  .brand-dot{width:22px;height:22px;border-radius:50%;background:var(--navy)}
  .brand-name{font-weight:700;font-size:22px;letter-spacing:.5px;color:var(--navy)}
  .sender{position:absolute;left:84px;top:206px;font-size:12px;line-height:17.5px}
  .sender-name{color:var(--cyan);font-weight:700;font-size:12.5px}
  .sender .label{color:var(--cyan);font-weight:700}
  .date{position:absolute;right:85px;top:272px;font-size:12.5px}
  .body-copy{position:absolute;left:84px;top:326px;width:530px;font-size:12.4px;line-height:15.5px}
  .body-copy p{margin-bottom:30.5px}
  .signature{position:absolute;left:84px;top:700px;font-family:"Open Sans",sans-serif;font-size:27px;color:var(--ink)}
  .signatory{position:absolute;left:84px;top:746px;font-size:12px;line-height:15px}
  .signatory strong{font-weight:700}
  .footer-shapes{position:absolute;left:0;top:814px}
  .contact-row{position:absolute;top:872px;left:0;width:696px;height:32px}
  .contact{position:absolute;top:0;display:flex;align-items:center;gap:9px;color:#fff;font-size:12.5px;line-height:15.5px}
  .contact svg{width:32px;height:32px;flex:none}
  .contact-phone{left:83px}
  .contact-mail{left:265px}
  .contact-place{left:455px}
</style>
</head>
<body>
<main class="letterhead">
  <div class="world-map" role="img" aria-label="Faint world map background"></div>

  <div class="brand">
    <span class="brand-dot"></span>
    <span class="brand-name">MORVESTA GROUP, LLC</span>
  </div>

  <section class="sender">
    <div class="sender-name">Elian Harrow</div>
    <div>Manager</div>
    <div><span class="label">A :</span> 1/2, your address here-123</div>
    <div><span class="label">E :</span> info@morvestagroup.com</div>
    <div><span class="label">P :</span> +00 123 456 7890</div>
  </section>

  <div class="date">Date. 10 May, 2021</div>

  <section class="body-copy">
    <p>Lorem Ipsum is simply dummy text of the printing and typesetting industry. Lorem Ipsum has been the industry's standard dummy text ever since the 1500s, when an unknown printer took a galley of type and scrambled it to make a type specimen book. It has survived not only five centuries, but also the leap into electronic typesetting,</p>
    <p>Lorem Ipsum is simply dummy text of the printing and typesetting industry. Lorem Ipsum has been the industry's standard dummy text ever since the 1500s, when an unknown printer took a galley of type and scrambled it to make a type specimen book. It has survived not only five centuries, but also the leap into electronic typesetting,</p>
    <p>Lorem Ipsum is simply dummy text of the printing and typesetting industry. Lorem Ipsum has been the industry's standard dummy text ever since the 1500s, when an unknown printer took a galley of type and scrambled it to make a type specimen book. It has survived not only five centuries, but also the leap into electronic typesetting,</p>
    <p>Lorem Ipsum is simply dummy text of the printing and typesetting industry. Lorem Ipsum has been the industry's standard dummy text ever since the 1500s, when an unknown printer took a galley of type.</p>
  </section>

  <div class="signature">Corin Vashti</div>
  <div class="signatory"><strong>Corin Vashti</strong><br>CEO</div>

  <svg class="footer-shapes" width="696" height="170" viewBox="0 0 696 170">
    <polygon points="0,0 140,0 170,32 0,32" fill="var(--cyan)"/>
    <polygon points="168,19 696,19 696,24 172,24" fill="var(--cyan)"/>
    <rect x="0" y="32" width="696" height="83" fill="var(--navy)"/>
    <polygon points="0,115 440,115 412,147 0,147" fill="var(--cyan)"/>
    <polygon points="499,137 696,137 696,170 469,170" fill="var(--cyan)"/>
  </svg>

  <div class="contact-row">
    <div class="contact contact-phone">
      <svg viewBox="0 0 32 32"><circle cx="16" cy="16" r="16" fill="var(--cyan)"/><path d="M11 9l3 0 1.5 4-2 1.5c1 2 2.5 3.5 4.5 4.5l1.5-2 4 1.5 0 3c-7 1-13.5-5.5-12.5-12.5z" fill="none" stroke="#fff" stroke-width="1.1" stroke-linejoin="round"/></svg>
      <span>+00 1234 5678<br>+00 1234 5678</span>
    </div>
    <div class="contact contact-mail">
      <svg viewBox="0 0 32 32"><circle cx="16" cy="16" r="16" fill="var(--cyan)"/><rect x="8" y="11" width="16" height="10" fill="none" stroke="#fff" stroke-width="1.1"/><path d="M8 11l8 6 8-6M8 21l6-5M24 21l-6-5" fill="none" stroke="#fff" stroke-width="1.1"/></svg>
      <span>info@example.com<br>www.example.com</span>
    </div>
    <div class="contact contact-place">
      <svg viewBox="0 0 32 32"><circle cx="16" cy="16" r="16" fill="var(--cyan)"/><path d="M16 25c-4-5-6-8-6-11a6 6 0 0 1 12 0c0 3-2 6-6 11z" fill="none" stroke="#fff" stroke-width="1.1"/><circle cx="16" cy="14" r="2.2" fill="none" stroke="#fff" stroke-width="1.1"/></svg>
      <span>Example Your Street<br>Address, City, 78694</span>
    </div>
  </div>
</main>
</body>
</html>
```